New audiology website PSD design only - guaranteed

We need a clean and attractive website to replace an existing Audiology (hearing technology) website which will be wordpress based.
The current website is: http://kvhearwell.com.au
They have a new logo and colors which you can find at www.qorvix.net/temp/kvh2018.pdf
We will no longer have a web shop in the new website
To enter the competition, we only need a sample of the home page.
The winning design will be asked to produce 2 standard page template alternatives as well (based on the winning home page design, but for a standard page layout)
The winning design must provide any photos used
We want a clean, credible site but with some warmth
Target Market(s)
All ages but needs to include the elderly
Industry/Entity Type
Medical And Science
Number of Pages Required
3 page
Look and feel
Each slider illustrates characteristics of the customer's brand and the style your logo design should communicate.

```html
<!DOCTYPE html>
<html lang="en">
<head>
<meta charset="utf-8">
<title>KVHearwell – Hearing and Balance Clinic</title>
<link rel="stylesheet" href="https://fonts.googleapis.com/css2?family=Poppins:wght@300;400;500;600&family=Noto+Serif:ital@1&display=swap">
<style>
:root{
  --orange:#f37021;
  --orange-dark:#e2621a;
  --charcoal:#3f3f41;
  --ink:#2b2b2b;
  --text:#666;
  --soft:#f2f2f2;
  --line:#dcdcdc;
  --white:#fff;
}
*{margin:0;padding:0;box-sizing:border-box}
html,body{width:1200px;height:2353px;overflow:hidden}
body{font-family:'Poppins',sans-serif;color:var(--text);background:var(--white);position:relative}
a{color:inherit;text-decoration:none}

.topbar{height:34px;background:var(--orange);color:var(--white);font-size:12.5px;font-weight:500;text-align:center;line-height:34px}

.nav{height:63px;background:var(--white);position:relative}
.brand{position:absolute;left:172px;top:16px;display:flex;align-items:center;gap:8px;font-size:24px;font-weight:500;color:var(--ink)}
.brand-dot{width:26px;height:26px;border-radius:50%;border:2px solid var(--orange)}
.menu{position:absolute;left:424px;top:25px;display:flex;gap:18px;font-size:11.5px;font-weight:500;color:#555;white-space:nowrap}
.menu .active{color:var(--orange)}

.hero{height:452px;position:relative;overflow:hidden}
.hero-photo{position:absolute;inset:0;background:linear-gradient(100deg,#9a5a43 0%,#c98b6e 30%,#e0c6a8 52%,#ece5d9 75%,#f4f2ee 100%)}
.hero-shade{position:absolute;inset:0;background:rgba(0,0,0,.18)}
.hero-copy{position:absolute;left:0;right:0;top:190px;text-align:center;color:var(--white)}
.hero-copy h1{font-size:23px;font-weight:500;line-height:1.34;width:460px;margin:0 auto;text-shadow:0 1px 3px rgba(0,0,0,.3)}
.btn{display:inline-block;background:var(--orange);color:var(--white);font-size:12px;font-weight:500;padding:10px 19px;border-radius:2px;white-space:nowrap}
.hero-copy .btn{margin-top:22px}
.dots{position:absolute;left:0;right:0;bottom:18px;display:flex;justify-content:center;gap:5px}
.dots span{width:10px;height:10px;border-radius:50%;background:rgba(255,255,255,.8)}
.dots span:first-child{background:var(--orange)}

.callband{height:74px;display:flex;position:relative}
.callband-left{width:600px;background:var(--orange);color:var(--white);display:flex;align-items:center;padding-left:171px;gap:8px}
.callband-left em{font-family:'Noto Serif',serif;font-style:italic;font-size:19px}
.callband-left strong{font-size:23px;font-weight:500}
.callband-arrow{position:absolute;left:600px;top:24px;width:0;height:0;border-top:13px solid transparent;border-bottom:13px solid transparent;border-left:13px solid var(--orange);z-index:2}
.callband-right{flex:1;background:var(--charcoal);color:var(--white);font-size:12px;line-height:1.45;padding:20px 0 0 42px}

.services{height:522px;background:var(--soft);position:relative}
.eyebrow{color:var(--orange);font-size:12px;text-align:center}
.section-title{color:var(--ink);font-size:22px;font-weight:500;text-align:center}
.services .eyebrow{padding-top:62px}
.service-list{position:absolute;top:172px;list-style:none;font-size:11.5px;color:#555}
.service-list li{height:36.5px;border-bottom:1px solid var(--line);display:flex;align-items:center;gap:10px;white-space:nowrap}
.service-list li:last-child{border-bottom:none}
.service-list.left{left:172px;width:252px}
.service-list.left li{justify-content:flex-end}
.service-list.right{left:778px;width:252px}
.ring{width:8px;height:8px;border-radius:50%;border:1.5px solid var(--orange);flex:none}
.service-visual{position:absolute;left:466px;top:122px;width:268px;height:268px;border-radius:50%;background:var(--white);box-shadow:0 2px 8px rgba(0,0,0,.12);padding:10px}
.service-visual div{width:100%;height:100%;border-radius:50%;background:radial-gradient(circle at 55% 50%,#f58a45,var(--orange) 70%)}
.services .btn{position:absolute;left:533px;top:425px}

.welcome{height:432px;position:relative;background:var(--white);overflow:hidden}
.welcome-photo{position:absolute;left:643px;top:0;width:557px;height:432px;background:linear-gradient(90deg,rgba(255,255,255,1) 0%,rgba(200,200,200,.6) 25%,#8d8f93 55%,#5e6066 100%)}
.welcome-copy{position:absolute;left:172px;top:46px;width:490px}
.welcome-copy .eyebrow{text-align:left;margin-bottom:0;line-height:1.5}
.welcome-copy h2{color:var(--ink);font-size:23px;font-weight:500;margin-bottom:14px;line-height:1.3}
.welcome-copy p.body{font-size:11.6px;line-height:1.82;margin-bottom:20px}
.welcome-copy .btn{margin-top:6px}

.makers{height:412px;background:var(--charcoal);position:relative}
.makers .eyebrow{padding-top:60px}
.makers .section-title{color:var(--white)}
.maker-grid{position:absolute;left:172px;top:125px;width:856px;height:227px;background:var(--white);display:grid;grid-template-columns:repeat(4,1fr);grid-template-rows:repeat(2,1fr)}
.maker-grid span{display:flex;align-items:center;justify-content:center;font-size:26px;font-weight:500;color:#9a9a9a;border-right:1px solid #ececec;border-bottom:1px solid #ececec}
.maker-grid span:nth-child(4n){border-right:none}
.maker-grid span:nth-child(n+5){border-bottom:none}

.footer{height:364px;background:var(--orange);color:var(--white);position:relative;font-size:11.5px;line-height:1.7}
.footer h4{font-size:12.5px;font-weight:600;margin-bottom:10px}
.footer-col{position:absolute;top:58px}
.footer-col p+p{margin-top:18px}
.footer-brand{position:absolute;left:830px;top:58px}
.footer-brand .brand{position:static;color:var(--white)}
.footer-brand .brand-dot{border-color:var(--white)}
.footer-brand h4{margin-top:28px;margin-bottom:8px}
.socials{display:flex;gap:7px}
.socials span{width:27px;height:27px;border:2px solid var(--white)}
.copyright{position:absolute;left:0;right:0;top:281px;text-align:center;font-size:11.5px;line-height:1.7}
</style>
</head>
<body>

<div class="topbar">Speak to KV Audiologist Today! - (02) 9000 4821 &nbsp;|&nbsp; Trading Hours: Monday to Friday - 9am to 5pm</div>

<header class="nav">
  <a class="brand" href="#"><span class="brand-dot"></span>KVHearwell</a>
  <nav class="menu">
    <a class="active" href="#">Your Hearing</a>
    <a href="#">Hearing Aids</a>
    <a href="#">Musicians</a>
    <a href="#">Doctors Information</a>
    <a href="#">About Us</a>
    <a href="#">Products</a>
    <a href="#">Contact Us</a>
  </nav>
</header>

<section class="hero">
  <div class="hero-photo" role="img" aria-label="Smiling young couple embracing at home"></div>
  <div class="hero-shade"></div>
  <div class="hero-copy">
    <h1>KVHearwell is a leading Hearing and Balance Clinic located in the inner suburbs of Sydney.</h1>
    <a class="btn" href="#">Appointment Today!</a>
  </div>
  <div class="dots"><span></span><span></span><span></span><span></span><span></span></div>
</section>

<section class="callband">
  <div class="callband-left"><em>Call for an Appointment</em><strong>(02) 9000 4821</strong></div>
  <div class="callband-arrow"></div>
  <div class="callband-right">We will ensure a same-day appointment for all urgent Audiograms<br>and the earliest possible time for more complex testing.</div>
</section>

<section class="services">
  <p class="eyebrow">KVHearwell's Diagnostic</p>
  <h2 class="section-title">Services We Offer</h2>
  <ul class="service-list left">
    <li>Adult Hearing Test<span class="ring"></span></li>
    <li>Paediatric Hearing Test<span class="ring"></span></li>
    <li>Auditory Brainstem Response<span class="ring"></span></li>
    <li>VideoNystagmography (VNG)<span class="ring"></span></li>
    <li>Caloric Testing<span class="ring"></span></li>
  </ul>
  <div class="service-visual"><div role="img" aria-label="Hand holding a behind-the-ear hearing aid on orange"></div></div>
  <ul class="service-list right">
    <li><span class="ring"></span>Cortical Evoked Response Audiometry</li>
    <li><span class="ring"></span>Auditory Steady State Response</li>
    <li><span class="ring"></span>Vestibular Evoked Myogenic Potentials</li>
    <li><span class="ring"></span>Electrocochleography</li>
    <li><span class="ring"></span>Tinnitus</li>
  </ul>
  <a class="btn" href="#">View All Services</a>
</section>

<section class="welcome">
  <div class="welcome-photo" role="img" aria-label="Audiologist talking with an older patient"></div>
  <div class="welcome-copy">
    <p class="eyebrow">Welcome</p>
    <h2>KVHearwell</h2>
    <p class="body">KVHearwell is an independently owned and managed professional audiology clinic. Our Audiologists are health-care professionals specialising in diagnosing, treating and monitoring everything to do with hearing and balance. At KVHearwell we work closely with Ear, Nose and Throat specialists to ensure you receive the highest standards of medical care.</p>
    <p class="body">KVHearwell are state of the art hearing and balance clinics. We provide all brands of digital hearing aids, cochlear implants and assisted listening devices. We are diagnostic clinics, offering hearing tests for adults and children, balance tests, tinnitus testing and treatment, and auditory processing tests (APD).</p>
    <a class="btn" href="#">Learn More</a>
  </div>
</section>

<section class="makers">
  <p class="eyebrow">Our</p>
  <h2 class="section-title">Manufacturers</h2>
  <div class="maker-grid">
    <span>Auralis</span><span>Tonvia</span><span>Clarent</span><span>Sonmer</span>
    <span>Veltra</span><span>Brightear</span><span>Norvel</span><span>Halden</span>
  </div>
</section>

<footer class="footer">
  <div class="footer-col" style="left:172px">
    <h4>Contact Info</h4>
    <p>Eastholm<br>Ground Floor, Suite 3,<br>&nbsp;18 Larkin Parade,<br>Eastholm, NSW, 2190</p>
    <p>Ph: 9000 4821<br>Email us</p>
  </div>
  <div class="footer-col" style="left:392px">
    <h4>&nbsp;</h4>
    <p>Westmere<br>Shop 2, 41 Harbour<br>Road Westmere,<br>NSW, 2191</p>
    <p>Ph: 9000 7365<br>Email us</p>
  </div>
  <div class="footer-col" style="left:610px">
    <h4>Quick Links</h4>
    <p>Your Hearing<br>Hearing Aids<br>Musicians<br>Doctors Information<br>About Us<br>Products<br>Contact Us</p>
  </div>
  <div class="footer-brand">
    <a class="brand" href="#"><span class="brand-dot"></span>KVHearwell</a>
    <h4>Stay Connected</h4>
    <div class="socials"><span></span><span></span><span></span></div>
  </div>
  <p class="copyright">Copyright © Kingsvale Hearwell. All Rights Reserved<br>Terms and Conditions</p>
</footer>

</body>
</html>
```